Small ad for an eye doctor on pharmacy bag

We need a small ad for an eye doctor which will be placed on a pharmacy bag. The colors are black and red, the bag itself is white. The size is only 4.25 x 1.5 inches. The ad will be placed among other ads, and we are looking for something a little more modern and bold that will stick out. (See attached sample: We will be replacing the third ad on the second page, which is Brisk Box&Post/Parcelon).
The copy is:
Dr. Miriam Tollbeck MD
Best Eye Doctor in Brooklyn
Tel. (718) 555-0163
27 Larchmont Lane
www.ClearviewOpticsHub.example
You don't necessarily have to use the logo or even her photo, we are just trying to provide you with some elements to play with.
Target Market(s)
Pharmacy clients in Brooklyn
Industry/Entity Type
Doctor

```html
<!DOCTYPE html>
<html lang="en">
<head>
<meta charset="utf-8">
<title>Dr. Miriam Tollbeck MD – Bag Ad Options</title>
<link href="https://fonts.googleapis.com/css2?family=Cinzel:wght@700&family=PT+Serif:wght@700&family=Montserrat:wght@500&display=swap" rel="stylesheet">
<style>
  :root {
    --canvas: #cccccc;
    --card: #ffffff;
    --card-edge: #8a8a8a;
    --band-blue: #11618a;
    --band-grey: #4d4d4d;
    --ink: #3d3d3d;
    --on-band: #ffffff;
  }
  html, body {
    margin: 0;
    padding: 0;
    width: 1200px;
    height: 1000px;
    overflow: hidden;
    background: var(--canvas);
  }
  .canvas {
    position: relative;
    width: 1200px;
    height: 1000px;
  }
  .ad {
    position: absolute;
    left: 158px;
    width: 882px;
    height: 310px;
    background: var(--card);
    border: 1px solid var(--card-edge);
    overflow: hidden;
  }
  .ad--color { top: 155px; }
  .ad--mono { top: 533px; }
  .ad__band {
    height: 94px;
    display: flex;
    align-items: center;
    justify-content: center;
    color: var(--on-band);
    font-family: "Cinzel", "Times New Roman", serif;
    font-weight: 700;
    font-size: 44px;
    letter-spacing: 0.5px;
  }
  .ad--color .ad__band { background: var(--band-blue); }
  .ad--mono .ad__band { background: var(--band-grey); }
  .ad__portrait {
    position: absolute;
    left: 28px;
    top: 104px;
    width: 220px;
    height: 206px;
    border-radius: 90px 90px 0 0;
  }
  .ad--color .ad__portrait {
    background: linear-gradient(180deg, #6b4a35 0%, #d9a58c 35%, #eef1f2 70%, #f7f8f8 100%);
  }
  .ad--mono .ad__portrait {
    background: linear-gradient(180deg, #444 0%, #9a9a9a 35%, #e9e9e9 70%, #f6f6f6 100%);
  }
  .ad__headline {
    position: absolute;
    left: 240px;
    right: 40px;
    top: 106px;
    text-align: center;
    font-family: "PT Serif", Georgia, serif;
    font-weight: 700;
    color: var(--ink);
    margin: 0;
  }
  .ad__headline-best {
    display: block;
    font-size: 90px;
    line-height: 100px;
  }
  .ad__headline-rest {
    display: block;
    font-size: 50px;
    line-height: 56px;
    margin-left: 14px;
  }
  .ad__contacts {
    position: absolute;
    left: 244px;
    top: 274px;
    display: flex;
    gap: 22px;
    font-family: "Montserrat", Arial, sans-serif;
    font-weight: 500;
    font-size: 15px;
    color: var(--ink);
  }
  .contact {
    display: flex;
    align-items: center;
    gap: 6px;
    white-space: nowrap;
  }
  .contact svg { width: 17px; height: 17px; flex: none; }
</style>
</head>
<body>
<div class="canvas">

  <section class="ad ad--color">
    <div class="ad__band">Dr. Miriam Tollbeck MD</div>
    <div class="ad__portrait" role="img" aria-label="Portrait photo of the doctor in a white coat"></div>
    <h1 class="ad__headline">
      <span class="ad__headline-best">Best</span>
      <span class="ad__headline-rest">Eye Doctor in Brooklyn</span>
    </h1>
    <div class="ad__contacts">
      <span class="contact">
        <svg viewBox="0 0 20 20"><circle cx="10" cy="10" r="10" fill="#3d3d3d"/><path d="M6 14 L14 6" stroke="#fff" stroke-width="2.4" stroke-linecap="round"/></svg>
        (718) 555-0163
      </span>
      <span class="contact">
        <svg viewBox="0 0 20 20"><circle cx="10" cy="10" r="10" fill="#3d3d3d"/><path d="M10 15 C7 11 6.5 9.8 6.5 8.5 A3.5 3.5 0 0 1 13.5 8.5 C13.5 9.8 13 11 10 15Z" fill="#fff"/><circle cx="10" cy="8.5" r="1.3" fill="#3d3d3d"/></svg>
        27 Larchmont Lane
      </span>
      <span class="contact">
        <svg viewBox="0 0 20 20"><circle cx="10" cy="10" r="10" fill="#3d3d3d"/><circle cx="10" cy="10" r="5" fill="none" stroke="#fff" stroke-width="1.5"/><path d="M5 10 H15 M10 5 V15" stroke="#fff" stroke-width="1.2"/></svg>
        www.ClearviewOpticsHub.example
      </span>
    </div>
  </section>

  <section class="ad ad--mono">
    <div class="ad__band">Dr. Miriam Tollbeck MD</div>
    <div class="ad__portrait" role="img" aria-label="Black and white portrait photo of the doctor in a white coat"></div>
    <h1 class="ad__headline">
      <span class="ad__headline-best">Best</span>
      <span class="ad__headline-rest">Eye Doctor in Brooklyn</span>
    </h1>
    <div class="ad__contacts">
      <span class="contact">
        <svg viewBox="0 0 20 20"><circle cx="10" cy="10" r="10" fill="#3d3d3d"/><path d="M6 14 L14 6" stroke="#fff" stroke-width="2.4" stroke-linecap="round"/></svg>
        (718) 555-0163
      </span>
      <span class="contact">
        <svg viewBox="0 0 20 20"><circle cx="10" cy="10" r="10" fill="#3d3d3d"/><path d="M10 15 C7 11 6.5 9.8 6.5 8.5 A3.5 3.5 0 0 1 13.5 8.5 C13.5 9.8 13 11 10 15Z" fill="#fff"/><circle cx="10" cy="8.5" r="1.3" fill="#3d3d3d"/></svg>
        27 Larchmont Lane
      </span>
      <span class="contact">
        <svg viewBox="0 0 20 20"><circle cx="10" cy="10" r="10" fill="#3d3d3d"/><circle cx="10" cy="10" r="5" fill="none" stroke="#fff" stroke-width="1.5"/><path d="M5 10 H15 M10 5 V15" stroke="#fff" stroke-width="1.2"/></svg>
        www.ClearviewOpticsHub.example
      </span>
    </div>
  </section>

</div>
</body>
</html>
```